LED Bulb Packaging

We require a retail box design so some led lighting. The concept must be uniform accross a nuimber of sizes with technical information and Actual bulb image replaceable.

```html
<!DOCTYPE html>
<html lang="en">
<head>
<meta charset="utf-8">
<title>LED Corn Light 27W – Retail Box Dieline</title>
<link href="https://fonts.googleapis.com/css2?family=Arimo:wght@400;700&family=Noto+Serif+SC:wght@400&display=swap" rel="stylesheet">
<style>
  :root{
    --orange:#f08a24;
    --red:#e8222a;
    --ink:#222222;
    --flap:#c9c7c3;
    --cut:#e9a3b4;
    --paper:#ffffff;
    --bulb-dark:#6f7378;
    --bulb-light:#e4e6e8;
  }
  html,body{margin:0;padding:0;overflow:hidden;background:var(--paper);}
  .canvas{position:relative;width:1200px;height:483px;overflow:hidden;background:var(--paper);}
  .size-title{
    position:absolute;left:0;right:0;top:0;margin:0;
    text-align:center;padding-left:38px;
    font-family:"Arimo","Noto Serif SC",sans-serif;font-weight:400;
    font-size:66px;line-height:74px;color:var(--red);letter-spacing:2px;
  }
  .size-title .cjk{font-family:"Noto Serif SC",serif;}
  .size-title .colon{margin:0 18px;}
  .dieline{position:absolute;left:0;top:0;}
  .cut{fill:none;stroke:var(--cut);stroke-width:1;}
  .panel{fill:var(--paper);stroke:var(--cut);stroke-width:1;}
  .flap{fill:var(--flap);stroke:var(--cut);stroke-width:1;}
  .rule{fill:var(--orange);}
  .txt{font-family:"Arimo",sans-serif;}
  .led{font-weight:700;fill:var(--orange);}
  .corn{font-weight:700;fill:var(--ink);}
  .spec{font-weight:700;fill:var(--orange);}
  .spec-label{fill:var(--ink);font-size:5px;}
  .note-title{font-weight:700;fill:var(--orange);font-size:11px;letter-spacing:1px;}
  .note-line{fill:var(--ink);font-size:5.6px;}
  .brand{font-weight:700;fill:var(--orange);}
  .feature-label{fill:var(--ink);font-size:5px;text-anchor:middle;}
  .badge{fill:none;stroke:#555;stroke-width:1.2;}
  .wattage{font-weight:700;fill:var(--orange);font-size:36px;text-anchor:middle;}
  .bullets{fill:var(--ink);font-size:9px;text-anchor:middle;}
</style>
</head>
<body>
<div class="canvas">
  <h1 class="size-title">27W<span class="cjk">尺寸</span><span class="colon">:</span>250*95*95mm</h1>

  <svg class="dieline" width="1200" height="483" viewBox="0 0 1500 604" xmlns="http://www.w3.org/2000/svg">
    <defs>
      <linearGradient id="bulbTone" x1="0" y1="0" x2="1" y2="0">
        <stop offset="0" stop-color="var(--bulb-dark)"/>
        <stop offset="0.45" stop-color="var(--bulb-light)"/>
        <stop offset="1" stop-color="#9aa0a6"/>
      </linearGradient>
    </defs>

    <g class="side-left">
      <polygon class="cut" points="0,355 40,340 40,490 0,472"/>
      <polygon class="flap" points="40,340 108,262 365,262 435,340"/>
      <rect class="rule" x="108" y="268" width="257" height="3"/>
      <text class="txt led" x="237" y="294" font-size="17" text-anchor="middle">LED</text>
      <text class="txt corn" x="237" y="302" font-size="6" text-anchor="middle">CORN LIGHT</text>
      <rect class="rule" x="155" y="336" width="163" height="4"/>
      <rect class="rule" x="205" y="308" width="63" height="62"/>
      <rect class="panel" x="40" y="340" width="395" height="150"/>
      <rect class="rule" x="205" y="340" width="63" height="30"/>
      <polygon class="flap" points="40,490 435,490 375,545 335,560 335,604 140,604 140,560 100,545"/>
      <text class="txt led" x="56" y="385" font-size="36">LED</text>
      <text class="txt corn" x="57" y="401" font-size="13">CORN LIGHT</text>
      <text class="txt spec" x="57" y="428" font-size="13">120lm/w</text>
      <text class="txt spec-label" x="57" y="434">Luminous efficiency</text>
      <text class="txt corn" x="142" y="422" font-size="5">UP</text>
      <text class="txt corn" x="142" y="428" font-size="5">TO</text>
      <text class="txt spec" x="152" y="428" font-size="12">85%</text>
      <text class="txt spec-label" x="142" y="434">Energy Saving</text>
      <text class="txt spec" x="57" y="447" font-size="13">50000hrs</text>
      <text class="txt spec-label" x="57" y="454">Lifespan</text>
      <text class="txt spec" x="142" y="447" font-size="13">IP64</text>
      <g class="cert-row">
        <circle class="badge" cx="66" cy="469" r="6"/><circle class="badge" cx="89" cy="469" r="6"/>
        <circle class="badge" cx="110" cy="469" r="6"/><circle class="badge" cx="131" cy="469" r="6"/>
        <circle class="badge" cx="152" cy="469" r="6"/><circle class="badge" cx="174" cy="469" r="6"/>
      </g>
      <rect x="235" y="374" width="170" height="96" rx="18" fill="url(#bulbTone)" role="img" aria-label="Product photo: 27W LED corn light bulb with E-base"/>
    </g>

    <g class="side-note">
      <polygon class="cut" points="435,340 505,262 585,262 585,340"/>
      <rect class="rule" x="505" y="268" width="76" height="3"/>
      <rect class="panel" x="435" y="340" width="150" height="150"/>
      <polygon class="cut" points="435,490 585,490 585,604 505,604 505,560"/>
      <text class="txt note-title" x="440" y="354">Note:</text>
      <text class="txt note-line" x="440" y="365">1:Before install or replace the lamps please cut off</text>
      <text class="txt note-line" x="444" y="372">the switch.</text>
      <text class="txt note-line" x="440" y="379">2:After installed,when lamp work normal,pls note</text>
      <text class="txt note-line" x="444" y="386">not take off the driver with electriferous.</text>
      <text class="txt note-line" x="440" y="393">3:After lighting a long time,the lamps can be reach</text>
      <text class="txt note-line" x="444" y="400">60°C,Pls be careful to take off the lamps avoid scald.</text>
      <text class="txt note-line" x="440" y="407">4:Interior driver is constant current.</text>
      <text class="txt note-line" x="440" y="414">5:Work temperature is -20~40°C.</text>
      <g class="energy-label">
        <rect x="440" y="420" width="48" height="65" fill="#fff" stroke="#999" stroke-width="0.8"/>
        <rect x="475" y="423" width="10" height="8" fill="#1f4fa0"/>
        <polygon points="474,438 486,438 486,446 474,446 470,442" fill="#222"/>
        <rect x="442" y="437" width="10" height="5" fill="#1a9a3c"/>
        <rect x="442" y="443" width="13" height="5" fill="#52b33d"/>
        <rect x="442" y="449" width="16" height="5" fill="#a5c93a"/>
        <rect x="442" y="455" width="19" height="5" fill="#f2e41b"/>
        <rect x="442" y="461" width="22" height="5" fill="#f5b21a"/>
        <rect x="442" y="467" width="25" height="5" fill="#ee6f1f"/>
        <rect x="442" y="473" width="28" height="5" fill="#e3262b"/>
      </g>
    </g>

    <g class="front">
      <path d="M703,192 L703,160 Q703,152 711,152 L852,152 Q860,152 860,160 L860,192 Z" fill="var(--orange)"/>
      <path d="M740,192 L740,184 L828,184 L828,192" fill="var(--paper)"/>
      <rect class="panel" x="585" y="192" width="395" height="148"/>
      <g class="lid-art" transform="rotate(180 782.5 266)">
        <text class="txt brand" x="630" y="246" font-size="24" textLength="205" lengthAdjust="spacingAndGlyphs">NORVALE LIGHTING</text>
        <text class="txt corn" x="850" y="246" font-size="9">CORN LIGHT</text>
        <g class="features">
          <circle cx="662" cy="280" r="12" fill="var(--orange)"/><circle cx="662" cy="280" r="5" fill="none" stroke="#fff" stroke-width="1.5"/>
          <circle cx="697" cy="280" r="12" fill="var(--orange)"/><circle cx="697" cy="280" r="5" fill="none" stroke="#fff" stroke-width="1.5"/>
          <circle cx="732" cy="280" r="12" fill="var(--orange)"/><path d="M727,284 L732,273 L737,284 Z" fill="none" stroke="#fff" stroke-width="1.5"/>
          <circle cx="767" cy="280" r="12" fill="var(--orange)"/><text class="txt" x="767" y="285" font-size="13" font-weight="700" fill="#fff" text-anchor="middle">$</text>
          <circle cx="802" cy="280" r="12" fill="var(--orange)"/><ellipse cx="802" cy="280" rx="7" ry="4" fill="none" stroke="#fff" stroke-width="1.5"/><circle cx="802" cy="280" r="1.8" fill="#fff"/>
          <circle cx="837" cy="280" r="12" fill="var(--orange)"/><path d="M830,284 Q837,272 844,284" fill="none" stroke="#fff" stroke-width="1.5"/>
          <circle cx="872" cy="280" r="12" fill="var(--orange)"/><path d="M864,286 L880,274" stroke="#fff" stroke-width="1.5"/>
          <circle cx="907" cy="280" r="12" fill="var(--orange)"/><path d="M899,282 L903,277 L908,283 L915,277" fill="none" stroke="#fff" stroke-width="1.5"/>
          <text class="txt feature-label" x="662" y="300">High</text><text class="txt feature-label" x="662" y="306">Brightness</text>
          <text class="txt feature-label" x="697" y="300">Longlife</text>
          <text class="txt feature-label" x="732" y="300">Security</text>
          <text class="txt feature-label" x="767" y="300">Energy</text><text class="txt feature-label" x="767" y="306">Saving</text>
          <text class="txt feature-label" x="802" y="300">Protect</text><text class="txt feature-label" x="802" y="306">Your Eyes</text>
          <text class="txt feature-label" x="837" y="300">Green</text><text class="txt feature-label" x="837" y="306">Low-carbon</text>
          <text class="txt feature-label" x="872" y="300">No</text><text class="txt feature-label" x="872" y="306">Flicker Free</text>
          <text class="txt feature-label" x="907" y="300">No</text><text class="txt feature-label" x="907" y="306">Radiation</text>
        </g>
      </g>
      <rect class="panel" x="585" y="340" width="395" height="150"/>
      <polygon class="flap" points="585,490 980,490 980,575 930,575 930,604 880,604 880,575 685,575 685,604 635,604 635,575 585,575"/>
      <text class="txt led" x="600" y="385" font-size="36">LED</text>
      <text class="txt corn" x="601" y="401" font-size="13">CORN LIGHT</text>
      <text class="txt spec" x="601" y="428" font-size="13">120lm/w</text>
      <text class="txt spec-label" x="601" y="434">Luminous efficiency</text>
      <text class="txt corn" x="687" y="422" font-size="5">UP</text>
      <text class="txt corn" x="687" y="428" font-size="5">TO</text>
      <text class="txt spec" x="697" y="428" font-size="12">85%</text>
      <text class="txt spec-label" x="687" y="434">Energy Saving</text>
      <text class="txt spec" x="601" y="447" font-size="13">50000hrs</text>
      <text class="txt spec-label" x="601" y="454">Lifespan</text>
      <text class="txt spec" x="687" y="447" font-size="13">IP64</text>
      <g class="cert-row">
        <circle class="badge" cx="610" cy="469" r="6"/><circle class="badge" cx="633" cy="469" r="6"/>
        <circle class="badge" cx="654" cy="469" r="6"/><circle class="badge" cx="675" cy="469" r="6"/>
        <circle class="badge" cx="696" cy="469" r="6"/><circle class="badge" cx="718" cy="469" r="6"/>
      </g>
      <rect x="783" y="374" width="170" height="96" rx="18" fill="url(#bulbTone)" role="img" aria-label="Product photo: 27W LED corn light bulb with E-base"/>
    </g>

    <g class="side-right">
      <polygon class="cut" points="980,340 980,262 1058,262 1128,340"/>
      <rect class="rule" x="983" y="268" width="75" height="3"/>
      <rect class="panel" x="980" y="340" width="148" height="150"/>
      <polygon class="cut" points="980,490 1128,490 1058,560 1058,604 980,604"/>
      <text class="txt wattage" x="1054" y="444">27W</text>
      <text class="txt bullets" x="1052" y="478">•50000hrs  •IP64  •120lm/w</text>
    </g>

    <g class="insert">
      <rect class="panel" x="1210" y="300" width="290" height="265"/>
      <line class="cut" x1="1282" y1="300" x2="1282" y2="565"/>
      <line class="cut" x1="1428" y1="300" x2="1428" y2="565"/>
      <rect class="rule" x="1210" y="357" width="290" height="4"/>
      <rect class="rule" x="1210" y="439" width="290" height="4"/>
      <text class="txt led" x="1355" y="508" font-size="36" text-anchor="middle">LED</text>
      <text class="txt corn" x="1355" y="527" font-size="13" text-anchor="middle">CORN LIGHT</text>
    </g>
  </svg>
</div>
</body>
</html>
```